Local massage therapist needs some new marketing material

Hi there! I am a massage therapist here in Denver, CO in Willow Basin(shopping and art district) of the city. My business is called Lotus Drift Massage of Denver. My practice has an eastern influence and I do reflexology, thai massage and use Chinese herbs, etc. I know all my clients and pay close attention to details. I am also very respectful of tradition and it shows in how I work. I tend to like modern, clean, fun, Asian designs. I am wanting a new business card and brochure. I have a logo and branding for my business that I want used in the design. Currently, the sign for my building is purple and I think my logo was designed to be purple. I will attach pictures of it and can send whatever files are necessary so it can be integrated into the brochure, etc. I like the purple but open to using other colors as well. Thanks!
My website is lotusdriftmassagehub.example where info can be gathered about me and services/fees for brochure.
Updates

Just increased budget. Please see new feedback in discussion thread.

Thanks!

                                       HEY ALL,

Just wanted to let you know that I made a change to my website. It is on the Prices Page. I no longer have the frequent  flyer prices but I added discounts. Let me know if you have any questions. Thanks so much!

Target Market(s)

healthy, urban, educated, upper middle class, yogis

Industry/Entity Type

Marketing

Requirements
Must have
• logo stays purple
Should not have
• not too busy

```html
<!DOCTYPE html>
<html lang="en">
<head>
<meta charset="utf-8">
<title>Lotus Drift Massage of Denver – Services</title>
<link rel="stylesheet" href="https://fonts.googleapis.com/css2?family=Great+Vibes&family=Montserrat:wght@300;400;600&display=swap">
<style>
  :root {
    --magenta: #b5467a;
    --magenta-deep: #8e2a66;
    --plum: #7a2059;
    --cream: #e9e3cf;
    --sand: #c9bfa4;
    --stone: #8f8a78;
    --white: #ffffff;
    --ink: #2a2622;
  }
  html, body { margin: 0; padding: 0; overflow: hidden; }
  body { width: 1200px; height: 839px; background: var(--cream); }
  .brochure-panel {
    position: relative; width: 1200px; height: 839px; overflow: hidden;
    font-family: "Montserrat", sans-serif; color: var(--white);
  }
  .backdrop-photo {
    position: absolute; inset: 0;
    background:
      radial-gradient(ellipse at 70% 20%, #e6cfd6 0%, transparent 45%),
      radial-gradient(ellipse at 20% 55%, #bdb398 0%, transparent 55%),
      linear-gradient(120deg, #d3cbb3 0%, #a9a08a 40%, #cdb7b8 75%, #e2d3d2 100%);
  }
  .wave-layer { position: absolute; inset: 0; }
  .brand {
    position: absolute; left: 48px; top: 40px; width: 300px; text-align: center;
  }
  .brand-dot {
    width: 96px; height: 96px; border: 2px solid var(--white); border-radius: 50%;
    margin: 0 auto 56px;
  }
  .brand-name {
    font-weight: 300; font-size: 18px; letter-spacing: 2px; line-height: 24px;
    margin: 0; white-space: nowrap;
  }
  .therapist-photo {
    position: absolute; left: 92px; top: 278px; width: 207px; height: 207px;
    background: linear-gradient(160deg, #5f7f9a 0%, #3e5f7c 55%, #1f4f78 100%);
  }
  .bio {
    position: absolute; left: 22px; top: 512px;
    color: var(--ink); font-weight: 600; font-size: 9.6px; line-height: 12.6px;
    text-transform: uppercase; letter-spacing: 0.5px; white-space: nowrap;
  }
  .bio p { margin: 0 0 12.6px; }
  .bio p:last-child { margin: 0; }
  .bio .lead { font-size: 11px; }
  .services-title, .treats-title {
    position: absolute; margin: 0; font-weight: 400; text-align: center;
  }
  .services-title { left: 440px; top: 82px; width: 320px; font-size: 44px; }
  .treats-title { left: 850px; top: 124px; width: 300px; font-size: 31px; line-height: 34px; }
  .service-list, .treat-list {
    position: absolute; margin: 0; padding: 0; list-style: none;
    font-family: "Great Vibes", cursive; text-align: center;
    line-height: 80px; white-space: nowrap;
  }
  .service-list { left: 400px; top: 188px; width: 400px; font-size: 43px; }
  .service-list .seasonal { line-height: 42px; padding-bottom: 38px; }
  .treat-list { left: 820px; top: 226px; width: 360px; font-size: 40px; }
  .quote {
    position: absolute; left: 820px; top: 740px; width: 360px; margin: 0;
    text-align: center; font-weight: 300; font-size: 15px; line-height: 17px;
  }
</style>
</head>
<body>
<main class="brochure-panel">
  <div class="backdrop-photo" role="img" aria-label="Soft-focus photo of hands giving a back massage beside a lit candle and folded towels"></div>

  <svg class="wave-layer" viewBox="0 0 1200 839" width="1200" height="839" aria-hidden="true">
    <path d="M330 0 H1200 V700 C1050 640 850 690 700 760 C560 820 500 839 480 839 C470 700 430 560 340 430 C280 330 300 150 330 0 Z" fill="var(--magenta)" fill-opacity="0.82"/>
    <path d="M0 200 C100 210 200 250 300 300 L300 330 C200 285 100 252 0 245 Z" fill="var(--plum)" fill-opacity="0.55"/>
    <path d="M300 470 C420 560 560 700 680 839 H730 C610 700 460 560 300 492 Z" fill="var(--plum)" fill-opacity="0.85"/>
    <path d="M480 839 C620 760 800 700 980 690 C1080 686 1150 700 1200 720 V839 Z" fill="var(--plum)" fill-opacity="0.9"/>
    <path d="M0 495 C150 480 300 505 380 545 C470 600 560 720 640 839 H0 Z" fill="var(--cream)" fill-opacity="0.8"/>
  </svg>

  <header class="brand">
    <div class="brand-dot"></div>
    <p class="brand-name">Lotus Drift Massage of Denver</p>
  </header>

  <div class="therapist-photo" role="img" aria-label="Portrait photo of the massage therapist"></div>

  <section class="bio">
    <p><span class="lead">Clara Vennholt is</span><br>
    a registered massage therapist,<br>
    a member of the Guild for Gentle<br>
    Aromatherapy, Eastern Touch Circle,<br>
    Highland Bodywork Society, Quiet Hands Foundation<br>
    and Union of Bodywork Practitioners.</p>
    <p>She graduated from the Front Range<br>
    Bodywork College and has formally studied Thai<br>
    massage techniques at the Lanna Valley<br>
    Massage School, Thailand. Presently, she is studying at<br>
    Stillwater Healing Academy with students from around the<br>
    world to better understand natural health, energy work<br>
    and spiritual counseling. Clara began meditation as a teen and<br>
    learned the benefits of quieting the mind. Feeling the call within<br>
    herself to help others, Clara naturally gravitated toward massage<br>
    therapy and natural healing. Clara enjoys helping to facilitate people<br>
    on their journeys toward health and personal happiness. She believes in<br>
    an energy chi within us that when unobstructed, promotes our health<br>
    and well being.<br>
    She trusts in the body's natural capacity to heal, and takes advantage of this<br>
    power in her delivery of bodywork.</p>
  </section>

  <h2 class="services-title">Services</h2>
  <ul class="service-list">
    <li class="seasonal">Colorado Rain<br>(Seasonal Treatment)</li>
    <li>Swedish Escape</li>
    <li>Deep Tissue Therapy</li>
    <li>Table Thai Massage</li>
    <li>Blend Massage</li>
    <li>Prenatal Bliss</li>
  </ul>

  <h2 class="treats-title">Extra Massage<br>Treats</h2>
  <ul class="treat-list">
    <li>Chinese Fire Cupping</li>
    <li>Hot Stones</li>
    <li>Reflexology</li>
    <li>Thai Herbal Compress</li>
  </ul>

  <p class="quote">I invite you to take some time for<br>yourself, for there truly is<br>"more to life than increasing its speed".<br>-Ravi Anand</p>
</main>
</body>
</html>
```